Box Truck wrap for an insulation company

Full wrap design for a box truck.
The services we offer are

Target Market(s)

Homeowners

Industry/Entity Type

Home Improvement

Colors
acd136
0455a3

Requirements
Must have
• Lic# 3859160 (Small. Required by law)
559-318-2264 (large)
Www.Marlowheatworks.com
Logo (large)
We fix high utility bills

Insulation
Whole house fans
Insulation removal
Window film
Thermal imaging inspections
Solar
and more
Nice to have
• a blended collage of solar, insulation, and thermal imaging

```html
<!DOCTYPE html>
<html lang="en">
<head>
<meta charset="utf-8">
<title>Marlow Heatworks – Box Truck Wrap</title>
<link rel="stylesheet" href="https://fonts.googleapis.com/css2?family=Barlow+Condensed:wght@400;500;600;700&display=swap">
<style>
  :root {
    --brand-green: #acd136;
    --brand-blue: #0455a3;
    --deep-blue: #1d4592;
    --panel-white: #ffffff;
    --stage: #98a96d;
    --ink: #1a1a1a;
  }
  html, body {
    margin: 0;
    padding: 0;
    width: 1200px;
    height: 1200px;
    overflow: hidden;
    background: var(--stage);
  }
  .canvas {
    position: relative;
    width: 1200px;
    height: 1200px;
  }
  .wrap-panel {
    position: absolute;
    left: 60px;
    width: 1080px;
    height: 560px;
    display: block;
  }
  .wrap-panel--driver { top: 27px; }
  .wrap-panel--passenger { top: 613px; }
  .panel-text { font-family: "Barlow Condensed", sans-serif; }
  .brand-name { font-weight: 600; letter-spacing: 3px; fill: var(--brand-blue); }
  .service-blue { fill: var(--brand-blue); font-weight: 500; }
  .service-green { fill: #8cb428; font-weight: 500; }
  .headline { fill: var(--brand-blue); font-weight: 700; }
  .tagline { fill: var(--ink); font-weight: 400; }
  .license { fill: var(--ink); font-weight: 500; }
  .phone { fill: var(--panel-white); font-weight: 600; }
  .web { fill: var(--panel-white); font-weight: 400; }
</style>
</head>
<body>
<div class="canvas">
  <svg width="0" height="0" style="position:absolute">
    <defs>
      <linearGradient id="solar-tone" x1="0" y1="0" x2="1" y2="1">
        <stop offset="0" stop-color="#6fa8dc"/><stop offset="1" stop-color="#1f3f8a"/>
      </linearGradient>
      <linearGradient id="thermal-tone" x1="0" y1="0" x2="1" y2="1">
        <stop offset="0" stop-color="#c9b9a4"/><stop offset="1" stop-color="#4a4a4a"/>
      </linearGradient>
      <linearGradient id="insulation-tone" x1="0" y1="0" x2="1" y2="1">
        <stop offset="0" stop-color="#8a5a3a"/><stop offset="1" stop-color="#d8a5b8"/>
      </linearGradient>
      <linearGradient id="window-tone" x1="0" y1="0" x2="1" y2="1">
        <stop offset="0" stop-color="#7e9b5e"/><stop offset="1" stop-color="#cfd6d8"/>
      </linearGradient>
      <path id="house-icon" d="M0,-6 L7,0 L5,0 L5,6 L-5,6 L-5,0 L-7,0 Z"/>
      <g id="wrap-graphics">
        <rect x="0" y="0" width="810" height="420" fill="var(--panel-white)"/>
        <path d="M0,345 C250,382 430,380 600,296 L660,270 L660,292 C450,392 220,388 0,360 Z" fill="var(--deep-blue)"/>
        <path d="M0,360 C220,388 450,392 660,292 L810,225 L810,420 L0,420 Z" fill="var(--brand-green)"/>
        <g class="collage">
          <polygon points="660,0 770,0 715,55" fill="var(--brand-green)"/>
          <polygon points="718,90 810,0 810,180" fill="var(--deep-blue)"/>
          <polygon points="725,255 810,170 810,340" fill="var(--brand-green)"/>
          <polygon points="540,150 625,235 540,320" fill="var(--brand-green)"/>
          <polygon points="620,-20 700,60 620,140 540,60" fill="url(#solar-tone)" stroke="#fff" stroke-width="4" role="img" aria-label="Photo of a technician installing rooftop solar panels"/>
          <polygon points="730,80 815,165 730,250 645,165" fill="url(#thermal-tone)" stroke="#fff" stroke-width="4" role="img" aria-label="Photo of a thermal imaging camera pointed at a house"/>
          <polygon points="625,170 710,255 625,340 540,255" fill="url(#insulation-tone)" stroke="#fff" stroke-width="4" role="img" aria-label="Photo of a worker laying attic insulation"/>
          <polygon points="720,275 800,355 720,435 640,355" fill="url(#window-tone)" stroke="#fff" stroke-width="4" role="img" aria-label="Photo of window film being applied to glass"/>
        </g>
        <rect x="0" y="0" width="810" height="420" fill="none" stroke="#d9d9d9" stroke-width="2"/>
      </g>
    </defs>
  </svg>

  <!-- Driver side -->
  <svg class="wrap-panel wrap-panel--driver" viewBox="0 0 810 420" aria-label="Driver side box panel">
    <use href="#wrap-graphics"/>
    <rect x="17" y="27" width="75" height="45" rx="3" fill="var(--brand-blue)" role="img" aria-label="Accreditation badge"/>
    <g class="panel-text">
      <text class="license" x="430" y="55" font-size="20">Lic# 3859160</text>
      <rect x="250" y="100" width="26" height="26" fill="var(--brand-green)"/>
      <text class="brand-name" x="295" y="180" font-size="40" text-anchor="middle">MARLOW HEATWORKS</text>
      <g class="service-list" font-size="16">
        <use href="#house-icon" x="36" y="217" fill="var(--brand-green)"/><text class="service-green" x="53" y="226">Insulation</text>
        <use href="#house-icon" x="36" y="239" fill="var(--brand-blue)"/><text class="service-blue" x="53" y="248">Whole House Fans</text>
        <use href="#house-icon" x="36" y="261" fill="var(--brand-green)"/><text class="service-green" x="53" y="270">Insulation Removal</text>
        <use href="#house-icon" x="36" y="283" fill="var(--brand-blue)"/><text class="service-blue" x="53" y="292">Window Film</text>
        <use href="#house-icon" x="36" y="305" fill="var(--brand-green)"/><text class="service-green" x="53" y="314">Thermal Imaging Inspections</text>
        <use href="#house-icon" x="36" y="327" fill="var(--brand-blue)"/><text class="service-blue" x="53" y="336">Solar, And More</text>
      </g>
      <text class="headline" x="287" y="272" font-size="32">Free Estimates</text>
      <text class="tagline" x="291" y="298" font-size="22">We fix high utility bills</text>
      <text class="web" x="40" y="404" font-size="22">Www.Marlowheatworks.com</text>
      <text class="phone" x="393" y="400" font-size="38">559-318-2264</text>
    </g>
  </svg>

  <!-- Passenger side -->
  <svg class="wrap-panel wrap-panel--passenger" viewBox="0 0 810 420" aria-label="Passenger side box panel">
    <use href="#wrap-graphics" transform="translate(810,0) scale(-1,1)"/>
    <rect x="713" y="27" width="75" height="45" rx="3" fill="var(--brand-blue)" role="img" aria-label="Accreditation badge"/>
    <g class="panel-text">
      <text class="license" x="270" y="55" font-size="20">Lic# 3859160</text>
      <rect x="415" y="100" width="26" height="26" fill="var(--brand-green)"/>
      <text class="brand-name" x="512" y="180" font-size="40" text-anchor="middle">MARLOW HEATWORKS</text>
      <g class="service-list" font-size="16" text-anchor="end">
        <use href="#house-icon" x="768" y="217" fill="var(--brand-green)"/><text class="service-green" x="752" y="226">Insulation</text>
        <use href="#house-icon" x="768" y="239" fill="var(--brand-blue)"/><text class="service-blue" x="752" y="248">Whole House Fans</text>
        <use href="#house-icon" x="768" y="261" fill="var(--brand-green)"/><text class="service-green" x="752" y="270">Insulation Removal</text>
        <use href="#house-icon" x="768" y="283" fill="var(--brand-blue)"/><text class="service-blue" x="752" y="292">Window Film</text>
        <use href="#house-icon" x="768" y="305" fill="var(--brand-green)"/><text class="service-green" x="752" y="314">Thermal Imaging Inspections</text>
        <use href="#house-icon" x="768" y="327" fill="var(--brand-blue)"/><text class="service-blue" x="752" y="336">Solar, And More</text>
      </g>
      <text class="headline" x="334" y="282" font-size="32">Free Estimates</text>
      <text class="tagline" x="338" y="308" font-size="22">We fix high utility bills</text>
      <text class="phone" x="200" y="400" font-size="38">559-318-2264</text>
      <text class="web" x="487" y="404" font-size="22">Www.Marlowheatworks.com</text>
    </g>
  </svg>
</div>
</body>
</html>
```